Website redesign: OLU - Bright Reel Studio

Web Design Brief
I'm looking for a redesign of our website https://www.brightreel.studio/. The website is built with Wix.

We are an AI Video Production Agency named OLU that uses AI-technology to create videos for our clients. We use the platform vormetric.io to generate videos.

Use case:
A financial services company is looking for a way to transform their inhouse training content to video.
They visit brightreel.studio and submit a brief.
Several production packages are presented, and the company selects the one that suits them best. Pricing is agreed upon, and the company provides the necessary scripts and documentation.

As a growing agency, our web page's primary objective is to acquire business leads (companies seeking professional video services) and to communicate our unique AI-driven approach to video production. The landing page will include a form for potential clients to fill out their requirements, as well as a showcase of our AI's capabilities in video production.

We have not yet chosen a color palette, but we are looking for a design that will inspire confidence in our clients while also highlighting the innovative and creative nature of our service. The overall theme should be sleek, modern, and visual, as our core offering is video creation and editing.

Current website:
https://www.brightreel.studio/

Competitors:
https://www.clipforge.pro/
https://pixelbound.ai/
https://www.quillspots.com/vormetric

Inspiration:
https://www.vormetric.io/
https://lumo.co.uk/
https://crispnorth.co/
https://www.bluefennel.com/

Target Market(s)

Director's of training and others who work with video at companies with $10M+ in revenue and 100+ employees.

Industry/Entity Type

Video Services Agency

Coding

Coded - Design and coding required

Number of Pages Required

1 page

Font styles to use
Sans Serif

Requirements
Must have
• Clear CTA and services showcase above the fold. Include "Services" and "Blog" section.
Nice to have
• Reviews / Proof of concept

```html
<!DOCTYPE html>
<html lang="en">
<head>
<meta charset="utf-8">
<title>OLU - Bright Reel Studio</title>
<link href="https://fonts.googleapis.com/css2?family=Montserrat:ital,wght@0,400;0,500;0,600;0,700;1,400&display=swap" rel="stylesheet">
<style>
:root{
  --blue:#1466dc;
  --blue-deep:#0b56c9;
  --cyan:#19a7ea;
  --ink:#2a2f3a;
  --muted:#4a5160;
  --pale:#e6f1fc;
  --pale-2:#f3f8fe;
  --white:#ffffff;
  --line:#dfe6ef;
}
*{box-sizing:border-box;margin:0;padding:0}
html,body{width:1200px;height:4866px;overflow:hidden}
body{position:relative;font-family:"Montserrat",sans-serif;color:var(--ink);background:var(--white)}
.abs{position:absolute}
svg{display:block}

.brand{position:absolute;display:flex;align-items:center;gap:12px}
.brand-dot{width:54px;height:54px;border-radius:50%;border:5px solid var(--blue)}
.brand-text{color:var(--blue);font-weight:700;line-height:1}
.brand-name{font-size:46px;letter-spacing:2px}
.brand-tag{font-size:9px;letter-spacing:1.6px;margin-top:3px}
.nav{position:absolute;display:flex;gap:38px;font-size:13px;font-weight:500;color:var(--ink);letter-spacing:.4px}
.nav .active{color:var(--blue);text-decoration:underline}
.btn-contact{position:absolute;left:975px;top:34px;width:136px;height:38px;border-radius:19px;background:var(--blue);border:2px solid #fff;color:#fff;font-size:13px;font-weight:500;display:flex;align-items:center;justify-content:center}

.hero-title{position:absolute;left:89px;top:190px;width:520px;font-size:41px;line-height:48px;font-weight:700;color:var(--blue)}
.hero-title span{color:var(--cyan)}
.hero-copy{position:absolute;left:89px;top:410px;width:440px;font-size:13px;line-height:21px;color:var(--ink)}

.photo-ring{position:absolute;border-radius:50%;border:2px solid var(--blue);padding:8px;background:transparent}
.photo{width:100%;height:100%;border-radius:50%;display:flex;align-items:center;justify-content:center;color:#fff;font-weight:600;font-size:31px;letter-spacing:2px}
.play{position:absolute;width:96px;height:96px;border-radius:50%;background:linear-gradient(135deg,#2a86f0,var(--blue-deep));border:6px solid #d8e9fb;box-shadow:0 8px 20px rgba(20,102,220,.35);display:flex;align-items:center;justify-content:center}

.h-section{position:absolute;left:0;width:1200px;text-align:center;font-size:30px;font-weight:700;color:var(--blue);letter-spacing:1px}
.sub-title{font-size:17px;font-weight:600;color:var(--cyan);line-height:22px}
.small{font-size:12.5px;line-height:20px;color:var(--ink)}

.service{position:absolute;width:440px;display:flex;gap:22px}
.service-icon{flex:none;width:106px;height:106px;border-radius:50%;background:linear-gradient(135deg,#27a3f2,#0d5fd6);border:5px solid #d9ebfc;display:flex;align-items:center;justify-content:center}
.service h3{font-size:17px;font-weight:600;color:var(--cyan);margin:6px 0 8px}

.outline-btn{position:absolute;border:1.5px solid var(--blue);border-radius:22px;color:var(--blue);font-size:12.5px;font-weight:500;display:flex;align-items:center;justify-content:center;background:#fff;letter-spacing:.5px}

.quote{position:absolute;left:129px;top:2160px;width:410px;font-size:21px;line-height:27.5px;font-style:italic;color:var(--ink)}
.person{position:absolute;left:129px;top:2342px;display:flex;align-items:center;gap:18px}
.avatar{width:78px;height:78px;border-radius:50%;background:linear-gradient(135deg,#f2f4f7,#cfd6de);border:3px solid #e9eef4}
.person a{color:var(--blue);font-size:15px;font-weight:500;text-decoration:underline}
.person p{font-size:14px;margin-top:6px}

.step{position:absolute;width:220px;text-align:center}
.step p{font-size:13px;font-weight:600;line-height:19px;margin-top:10px;color:var(--ink)}

.review-card{position:absolute;left:170px;top:3071px;width:860px;height:410px;border-radius:60px;background:#fff;box-shadow:0 12px 40px rgba(40,90,160,.12)}
.arrow-btn{position:absolute;width:34px;height:34px;border-radius:50%;display:flex;align-items:center;justify-content:center}

.post{position:absolute;top:3682px;width:320px}
.post-img{width:320px;height:183px;border-radius:12px}
.post p{font-size:13px;line-height:20px;margin:16px 8px 0}
.post-meta{display:flex;align-items:center;gap:10px;margin:12px 8px 0;font-size:12px}
.post-meta a{color:var(--ink);text-decoration:underline;margin-left:22px;font-weight:500}

.brand-box{position:absolute;top:4218px;width:227px;height:99px;background:#fff;border:1px solid var(--line);border-radius:4px;display:flex;align-items:center;justify-content:center;gap:14px}
.brand-box .mark{width:50px;height:50px;border-radius:50%}
.brand-box .lbl{font-size:20px;font-weight:700;color:#3a3f48;letter-spacing:1px;line-height:18px;text-align:center}
.brand-box .lbl small{display:block;font-size:11px;letter-spacing:4px}

.field{position:absolute;background:#fff;border:1px solid var(--line);display:flex;align-items:flex-start;gap:10px;padding:12px 12px;font-size:12px;color:#6b7280}

.foot-nav{position:absolute;top:4754px;left:433px;display:flex;gap:30px;font-size:13px;font-weight:500}
.foot-nav .active{color:var(--blue);text-decoration:underline}
.social{position:absolute;top:4747px;width:32px;height:32px;border-radius:50%;background:var(--blue)}
.bottom-bar{position:absolute;left:0;top:4829px;width:1200px;height:37px;background:var(--blue-deep);color:#fff;font-size:12px;display:flex;align-items:center;justify-content:center}
</style>
</head>
<body>

<div class="abs" style="left:0;top:610px;width:1200px;height:2450px;background:linear-gradient(180deg,#fff 0%,#fff 14%,#e3effc 28%,#f7fbff 40%,#fff 46%,#fff 58%,#f3f8fe 66%,#e8f2fd 76%,#f6faff 90%,#ffffff 100%)"></div>
<div class="abs" style="left:0;top:3060px;width:1200px;height:1770px;background:linear-gradient(180deg,#eef5fd 0%,#e7f1fc 30%,#f7fbff 50%,#e9f2fc 75%,#eaf3fd 100%)"></div>

<svg class="abs" style="left:1030px;top:1830px" width="170" height="250" aria-hidden="true"><circle cx="140" cy="125" r="110" fill="none" stroke="#dbe8f7" stroke-width="18"/></svg>
<svg class="abs" style="left:0;top:2470px" width="160" height="260" aria-hidden="true"><circle cx="20" cy="130" r="110" fill="none" stroke="#dbe8f7" stroke-width="18"/></svg>
<svg class="abs" style="left:1070px;top:3420px" width="130" height="240" aria-hidden="true"><circle cx="120" cy="120" r="100" fill="none" stroke="#dbe8f7" stroke-width="18"/></svg>
<svg class="abs" style="left:0;top:4200px" width="170" height="260" aria-hidden="true"><circle cx="30" cy="130" r="110" fill="none" stroke="#dbe8f7" stroke-width="18"/></svg>

<svg class="abs" style="left:0;top:0" width="1200" height="610" aria-hidden="true">
  <defs>
    <linearGradient id="heroPale" x1="0" y1="0" x2="0" y2="1"><stop offset="0" stop-color="#ffffff"/><stop offset="1" stop-color="#d6e8fb"/></linearGradient>
    <linearGradient id="heroBlue" x1="0" y1="0" x2="1" y2="1"><stop offset="0" stop-color="#1d9cf0"/><stop offset="1" stop-color="#0c5fd9"/></linearGradient>
  </defs>
  <rect width="1200" height="610" fill="url(#heroPale)"/>
  <path d="M0,0 H620 C560,140 620,330 520,500 C470,575 300,560 180,520 C100,495 40,500 0,520Z" fill="#fff"/>
  <path d="M600,0 H1200 V610 H700 C800,560 760,470 700,420 C590,330 560,140 600,0Z" fill="url(#heroBlue)"/>
</svg>

<div class="brand" style="left:89px;top:28px">
  <div class="brand-dot"></div>
  <div class="brand-text"><div class="brand-name">OLU</div><div class="brand-tag">BRIGHT REEL STUDIO</div></div>
</div>
<nav class="nav" style="left:590px;top:45px"><span class="active">TRAINING</span><span>MARKETING</span><span>HOW?</span><span>MORE</span></nav>
<div class="btn-contact">CONTACT US</div>

<h1 class="hero-title">Grow your business by improving operations efficiency through <span>video powered by AI</span></h1>
<p class="hero-copy">OLU levels up your training and marketing teams thanks to high-quality and efficient video production powered by AI. You will combine the latest technology available with the</p>

<div class="photo-ring" style="left:659px;top:111px;width:458px;height:458px;border-color:#fff">
  <div class="photo" role="img" aria-label="Presenter portrait in front of a night city skyline" style="background:linear-gradient(160deg,#2b3040 0%,#5a4a44 50%,#1f2430 100%)"></div>
</div>
<div class="play" style="left:661px;top:421px"><svg width="30" height="32"><path d="M6,3 L27,16 L6,29Z" fill="none" stroke="#fff" stroke-width="3" stroke-linejoin="round"/></svg></div>

<div class="abs" style="left:171px;top:784px;width:220px;text-align:right">
  <div class="sub-title">Boost your<br>business efficiency</div>
  <p class="small" style="margin-top:4px">You can use video to automate different areas of your business such as Marketing, Training &amp; Onboarding.</p>
</div>
<div class="abs" style="left:446px;top:705px;width:284px;height:284px;border-radius:50%;border:14px solid var(--blue);display:flex;align-items:center;justify-content:center;color:var(--blue);font-weight:700;font-size:56px;letter-spacing:3px">OLU</div>
<div class="abs" style="left:777px;top:756px;width:250px">
  <div class="sub-title">Save 80% of your time</div>
  <p class="small" style="margin-top:4px">Your human expert in video edition will be working for you autonomously, saving your teams time.</p>
  <div class="sub-title" style="margin-top:18px">Save 80% of your budget</div>
  <p class="small" style="margin-top:4px">Forget about long and expensive production costs, you will make better quality videos for less money.</p>
</div>

<h2 class="h-section" style="top:1102px">SERVICES</h2>
<div class="service" style="left:121px;top:1204px">
  <div class="service-icon"><svg width="56" height="56"><circle cx="28" cy="28" r="20" fill="none" stroke="#fff" stroke-width="2.5"/><text x="28" y="34" text-anchor="middle" font-family="Montserrat,sans-serif" font-size="16" font-weight="700" fill="#fff">AI</text></svg></div>
  <div><h3>AI Enhanced Website Creation</h3><p class="small">Your Webmaster will be working with you to create your dream website or targeted landing pages that will increase your sales.</p></div>
</div>
<div class="service" style="left:631px;top:1194px">
  <div class="service-icon"><svg width="56" height="56"><rect x="8" y="10" width="36" height="36" rx="4" fill="none" stroke="#fff" stroke-width="2.5"/><path d="M14,22 H30 M14,30 H26 M14,38 H22 M32,40 L48,18" stroke="#fff" stroke-width="2.5" stroke-linecap="round"/></svg></div>
  <div><h3>AI Enhanced Copywritting</h3><p class="small">Your Copywriter will create stunning texts, blogs post, social media posts, newsletters, articles, and much more with the help of TextPilot that will power up your results.</p></div>
</div>
<div class="service" style="left:121px;top:1365px">
  <div class="service-icon"><svg width="56" height="56"><circle cx="24" cy="30" r="16" fill="none" stroke="#fff" stroke-width="2.5"/><circle cx="24" cy="30" r="7" fill="none" stroke="#fff" stroke-width="2.5"/><path d="M24,30 L46,10 M38,10 H46 V18" stroke="#fff" stroke-width="2.5" stroke-linecap="round" fill="none"/></svg></div>
  <div><h3>AI Enhanced SEO</h3><p class="small">Your SEO will find, target, and measure the results of the keywords using the latest AI SEO tools in the market that will level up your website visitors.</p></div>
</div>
<div class="service" style="left:631px;top:1365px">
  <div class="service-icon"><svg width="56" height="56"><circle cx="14" cy="14" r="7" fill="none" stroke="#fff" stroke-width="2.5"/><circle cx="42" cy="14" r="7" fill="none" stroke="#fff" stroke-width="2.5"/><circle cx="14" cy="42" r="7" fill="none" stroke="#fff" stroke-width="2.5"/><circle cx="42" cy="42" r="7" fill="none" stroke="#fff" stroke-width="2.5"/><path d="M21,14 H35 M14,21 V35 M42,21 V35 M21,42 H35" stroke="#fff" stroke-width="2.5"/></svg></div>
  <div><h3>AI Enhanced Social Media</h3><p class="small">Your Social Media Manager will be posting content, connecting with your audience, and targeting perfect ads to grow your potential customers.</p></div>
</div>

<div class="photo-ring" style="left:94px;top:1587px;width:454px;height:454px">
  <div class="photo" role="img" aria-label="Trainer portrait on a warm yellow background" style="background:linear-gradient(160deg,#f2cc86 0%,#c9955f 55%,#8a6246 100%)">TRAINING</div>
</div>
<div class="play" style="left:457px;top:1895px"><svg width="30" height="32"><path d="M6,3 L27,16 L6,29Z" fill="none" stroke="#fff" stroke-width="3" stroke-linejoin="round"/></svg></div>

<div class="abs" style="left:724px;top:1722px;width:320px">
  <div style="font-size:30px;font-weight:600;color:var(--blue);letter-spacing:1px">LET'S TALK</div>
  <p style="font-size:12px;line-height:24px;margin-top:8px;letter-spacing:.3px">WE WILL CONTACT YOU SHORTLY,<br>ALTERNATIVELY YOU CAN BOOK A FREE<br>15 MINUTES STRATEGY CALL.</p>
</div>
<div class="outline-btn" style="left:724px;top:1860px;width:157px;height:40px">BOOK NOW</div>

<p class="quote">I only provided screenshots of my app and its main features. Then OLU's creative process kicked in and the result was a great promo video that I uploaded on PlayMart and AppHarbor.</p>
<div class="person">
  <div class="avatar" role="img" aria-label="Client portrait"></div>
  <div><a>Marco Feld Arrieta</a><p>Senior Mobile App Engineer</p></div>
</div>

<div class="photo-ring" style="left:659px;top:2066px;width:458px;height:458px">
  <div class="photo" role="img" aria-label="Presenter in a studio with a dark signboard" style="background:linear-gradient(160deg,#3a3f45 0%,#4b5560 45%,#6a5548 100%)">MARKETING</div>
</div>
<div class="play" style="left:661px;top:2371px"><svg width="30" height="32"><path d="M6,3 L27,16 L6,29Z" fill="none" stroke="#fff" stroke-width="3" stroke-linejoin="round"/></svg></div>

<h2 class="h-section" style="top:2631px">OUR PROCESS</h2>
<svg class="abs" style="left:120px;top:2700px" width="960" height="220" aria-hidden="true">
  <defs>
    <linearGradient id="g1" x1="0" y1="0" x2="1" y2="1"><stop offset="0" stop-color="#ffb300"/><stop offset="1" stop-color="#ff2e7a"/></linearGradient>
    <linearGradient id="g2" x1="0" y1="0" x2="1" y2="1"><stop offset="0" stop-color="#ff2e7a"/><stop offset="1" stop-color="#1466dc"/></linearGradient>
    <linearGradient id="g3" x1="0" y1="0" x2="1" y2="1"><stop offset="0" stop-color="#19d3e0"/><stop offset="1" stop-color="#6a2bd8"/></linearGradient>
    <linearGradient id="g4" x1="0" y1="0" x2="1" y2="1"><stop offset="0" stop-color="#19d38a"/><stop offset="1" stop-color="#ff2ec8"/></linearGradient>
    <filter id="sh" x="-30%" y="-30%" width="160%" height="160%"><feDropShadow dx="6" dy="8" stdDeviation="6" flood-color="#7a8aa0" flood-opacity=".35"/></filter>
  </defs>
  <g font-family="Montserrat,sans-serif" font-size="120" font-weight="700" fill="none" stroke-width="5">
    <g transform="translate(122,110)">
      <circle r="90" fill="none" stroke="url(#g1)" stroke-width="5"/>
      <text x="-115" y="44" stroke="url(#g1)" fill="#fff">1</text>
      <circle r="58" fill="#fff" stroke="none" filter="url(#sh)"/>
      <g stroke="#333" stroke-width="2.5" fill="none"><rect x="-16" y="-20" width="32" height="40" rx="3"/><path d="M-9,-8 l3,3 5,-6 M4,-6 H10 M-9,4 l3,3 5,-6 M4,6 H10"/></g>
    </g>
    <g transform="translate(360,110)">
      <circle r="90" fill="none" stroke="url(#g2)" stroke-width="5"/>
      <text x="-115" y="44" stroke="url(#g2)" fill="#fff">2</text>
      <circle r="58" fill="#fff" stroke="none" filter="url(#sh)"/>
      <g stroke="#333" stroke-width="2.5" fill="none"><circle cy="-4" r="14"/><path d="M-8,8 L-12,22 L0,16 L12,22 L8,8"/></g>
    </g>
    <g transform="translate(598,110)">
      <circle r="90" fill="none" stroke="url(#g3)" stroke-width="5"/>
      <text x="-115" y="44" stroke="url(#g3)" fill="#fff">3</text>
      <circle r="58" fill="#fff" stroke="none" filter="url(#sh)"/>
      <g stroke="#333" stroke-width="2.5" fill="none"><circle cy="-10" r="8"/><path d="M-14,20 V8 Q0,-2 14,8 V20Z"/></g>
    </g>
    <g transform="translate(836,110)">
      <circle r="90" fill="none" stroke="url(#g4)" stroke-width="5"/>
      <text x="-115" y="44" stroke="url(#g4)" fill="#fff">4</text>
      <circle r="58" fill="#fff" stroke="none" filter="url(#sh)"/>
      <g stroke="#333" stroke-width="2.5" fill="none"><rect x="-8" y="-20" width="26" height="20"/><path d="M2,-14 L10,-10 L2,-6Z M-20,20 H20 M-14,20 V8 H0 V20"/><circle cx="-7" cy="0" r="5"/></g>
    </g>
  </g>
</svg>
<div class="step" style="left:132px;top:2912px"><p>Requirement<br>Gathering and<br>Understandinga</p></div>
<div class="step" style="left:370px;top:2912px"><p>Deliver best quality<br>service using latest<br>AI tools</p></div>
<div class="step" style="left:608px;top:2912px"><p>Combine scripts created<br>by AI and AI Avatars to<br>get video production</p></div>
<div class="step" style="left:846px;top:2912px"><p>Deliver with human<br>interaction.</p></div>

<div class="review-card"></div>
<h2 class="h-section" style="top:3143px">REVIEWS</h2>
<svg class="abs" style="left:574px;top:3208px" width="52" height="40" aria-hidden="true"><path d="M2,40 V22 Q2,4 20,0 V8 Q12,10 12,20 H22 V40Z M30,40 V22 Q30,4 48,0 V8 Q40,10 40,20 H50 V40Z" fill="var(--cyan)"/></svg>
<p class="abs" style="left:258px;top:3272px;width:684px;text-align:center;font-size:13.5px;line-height:24px;font-weight:500">Lorem Ipsum is simply dummy text of the printing and typesetting industry. Lorem Ipsum has been the industry's standard dummy text ever since the 1500s, when an unknown printer took a galley of type and scrambled it to make a type specimen book.</p>
<svg class="abs" style="left:538px;top:3356px" width="124" height="24" aria-hidden="true">
  <g fill="#f5b400"><path id="st" d="M11,1 L14,8 L21,8 L15.5,12.5 L17.5,20 L11,15.5 L4.5,20 L6.5,12.5 L1,8 L8,8Z"/><use href="#st" x="25"/><use href="#st" x="50"/><use href="#st" x="75"/></g>
  <path d="M111,1 L114,8 L121,8 L115.5,12.5 L117.5,20 L111,15.5 L104.5,20 L106.5,12.5 L101,8 L108,8Z" fill="none" stroke="#f5b400" stroke-width="1.5"/>
  <path d="M111,1 L108,8 L101,8 L106.5,12.5 L104.5,20 L111,15.5Z" fill="#f5b400"/>
</svg>
<p class="abs" style="left:0;top:3388px;width:1200px;text-align:center;font-size:13px;color:var(--cyan)">- Nora P.</p>
<div class="arrow-btn" style="left:561px;top:3463px;background:#e1e4e9"><svg width="16" height="12"><path d="M15,6 H2 M6,1 L1,6 L6,11" stroke="#9aa2ad" stroke-width="1.6" fill="none"/></svg></div>
<div class="arrow-btn" style="left:603px;top:3463px;background:var(--blue)"><svg width="16" height="12"><path d="M1,6 H14 M10,1 L15,6 L10,11" stroke="#fff" stroke-width="1.6" fill="none"/></svg></div>

<h2 class="h-section" style="top:3610px">BLOG</h2>
<div class="post" style="left:89px">
  <div class="post-img" role="img" aria-label="Person with headphones editing video at a desk" style="background:linear-gradient(135deg,#c9a27a,#5c4a3c 55%,#2b2f36)"></div>
  <p>Lorem Ipsum is simply dummy text of the printing and typesetting...</p>
  <div class="post-meta"><svg width="14" height="14"><rect x="1" y="2" width="12" height="11" rx="2" fill="none" stroke="var(--blue)" stroke-width="1.5"/><path d="M1,6 H13" stroke="var(--blue)" stroke-width="1.5"/></svg>27 June, 2023<a>READ MORE</a></div>
</div>
<div class="post" style="left:440px">
  <div class="post-img" role="img" aria-label="Hands on a laptop showing a video editor" style="background:linear-gradient(135deg,#e8e6e2,#8a8e96 50%,#2a2d34)"></div>
  <p>Lorem Ipsum is simply dummy text of the printing and typesetting...</p>
  <div class="post-meta"><svg width="14" height="14"><rect x="1" y="2" width="12" height="11" rx="2" fill="none" stroke="var(--blue)" stroke-width="1.5"/><path d="M1,6 H13" stroke="var(--blue)" stroke-width="1.5"/></svg>27 June, 2023<a>READ MORE</a></div>
</div>
<div class="post" style="left:792px">
  <div class="post-img" role="img" aria-label="Laptop with floating blue video screens" style="background:linear-gradient(135deg,#0f1a2e,#1c4d86 55%,#6fb4e8)"></div>
  <p>Lorem Ipsum is simply dummy text of the printing and typesetting...</p>
  <div class="post-meta"><svg width="14" height="14"><rect x="1" y="2" width="12" height="11" rx="2" fill="none" stroke="var(--blue)" stroke-width="1.5"/><path d="M1,6 H13" stroke="var(--blue)" stroke-width="1.5"/></svg>27 June, 2023<a style="color:var(--blue)">READ MORE</a></div>
</div>
<div class="outline-btn" style="left:537px;top:4003px;width:128px;height:34px">VIEW ALL</div>

<h2 class="h-section" style="top:4148px">TRUSTED BRANDS</h2>
<div class="brand-box" style="left:104px"><div class="mark" style="background:#7ccf3a"></div><div class="lbl">LOREM<small>IPSUM</small></div></div>
<div class="brand-box" style="left:359px"><div class="mark" style="background:#f0a21a"></div><div class="lbl">LOREM<small>IPSUM</small></div></div>
<div class="brand-box" style="left:614px"><div class="mark" style="background:#1a8fd8"></div><div class="lbl">LOREM<small>IPSUM</small></div></div>
<div class="brand-box" style="left:869px"><div class="mark" style="background:#e0262c"></div><div class="lbl">LOREM<small>IPSUM</small></div></div>

<h2 class="h-section" style="top:4415px">QUICK INQUIRY</h2>
<div class="field" style="left:302px;top:4479px;width:290px;height:38px"><svg width="12" height="12"><circle cx="6" cy="4" r="3" fill="none" stroke="var(--blue)" stroke-width="1.3"/><path d="M1,12 Q6,5 11,12" fill="none" stroke="var(--blue)" stroke-width="1.3"/></svg>Name</div>
<div class="field" style="left:302px;top:4530px;width:290px;height:38px"><svg width="13" height="11"><rect x=".7" y=".7" width="11.6" height="9.6" fill="none" stroke="var(--blue)" stroke-width="1.3"/><path d="M1,1 L6.5,6 L12,1" fill="none" stroke="var(--blue)" stroke-width="1.3"/></svg>Email</div>
<div class="field" style="left:302px;top:4579px;width:290px;height:38px"><svg width="10" height="13"><rect x=".7" y=".7" width="8.6" height="11.6" rx="1.5" fill="none" stroke="var(--blue)" stroke-width="1.3"/></svg>Phone</div>
<div class="field" style="left:607px;top:4479px;width:291px;height:138px"><svg width="12" height="12"><rect x=".7" y=".7" width="10.6" height="10.6" fill="none" stroke="var(--blue)" stroke-width="1.3"/></svg>Message</div>
<div class="outline-btn" style="left:546px;top:4642px;width:108px;height:34px;font-size:14px">Submit</div>

<div class="brand" style="left:150px;top:4733px">
  <div class="brand-dot" style="width:46px;height:46px"></div>
  <div class="brand-text"><div class="brand-name" style="font-size:40px">OLU</div><div class="brand-tag" style="font-size:8px">BRIGHT REEL STUDIO</div></div>
</div>
<nav class="foot-nav"><span class="active">TRAINING</span><span>MARKETING</span><span>HOW?</span><span>MORE</span><span>CONTACT US</span></nav>
<div class="social" style="left:978px"></div>
<div class="social" style="left:1016px"></div>
<div class="bottom-bar">© 2023 OLU. All Right Reserved</div>

</body>
</html>
```